Mondeko Ltd

I have been recommended by my web builder to get a fully designed website from two different companies such as yourselves. I have 5 products initially and need a site with world wide appeal.

Target Market(s)

Care Home and Nail Bar Industry

Industry/Entity Type

Builder

Number of Pages Required

5+ page

Font styles to use
Sans Serif

Colors

Designer to choose colors to be used in the design.

Requirements
Must have
• Great Innovative Home Page
Nice to have
• I would like the background moving as in clouds rushing past. Similar to the way car lights are speeded up in night time ads. I have vel-tor quality shots of various cloud formations that I can send
Should not have
• Usual boring design

```html
<!DOCTYPE html>
<html lang="en">
<head>
<meta charset="utf-8">
<title>Mondeko Ltd</title>
<link rel="stylesheet" href="https://fonts.googleapis.com/css2?family=Open+Sans:ital,wght@0,400;0,600;0,700;1,400&family=Roboto+Condensed:wght@400;700&display=swap">
<style>
:root{
  --orange:#f7a21b;
  --blue:#1a86c8;
  --blue-dark:#0e6aa8;
  --navy:#1f4d8c;
  --teal:#1d6f78;
  --teal-dark:#134f57;
  --ink:#333;
  --muted:#666;
  --line:#d9d9d9;
  --paper:#ffffff;
  --mist:#f1f1f1;
  --dark:#2f2f2f;
}
*{margin:0;padding:0;box-sizing:border-box}
html,body{width:1200px;height:3346px;overflow:hidden}
body{font-family:"Open Sans",sans-serif;color:var(--ink);background:var(--paper);position:relative}
.section{position:absolute;left:0;width:1200px}
h2.section-title{font-family:"Roboto Condensed",sans-serif;font-weight:400;font-size:34px;text-align:center;letter-spacing:.5px;position:relative}

/* header */
.site-header{top:0;height:130px;background:var(--paper)}
.utility-bar{position:absolute;right:0;top:0;width:754px;height:36px;background:var(--orange);clip-path:polygon(40px 0,100% 0,100% 100%,0 100%)}
.utility-links{position:absolute;right:96px;top:7px;display:flex;gap:40px;align-items:center;font-size:12px;color:#fff}
.utility-links span{display:flex;align-items:center;gap:8px}
.utility-links .basket{background:var(--blue);color:#fff;border-radius:12px;padding:3px 14px;font-weight:600}
.brand{position:absolute;left:98px;top:30px;display:flex;align-items:center;gap:12px}
.brand-mark{width:34px;height:34px;border-radius:50%;background:var(--blue)}
.brand-name{font-family:"Open Sans",sans-serif;font-weight:700;font-size:36px;color:var(--navy)}
.main-nav{position:absolute;right:98px;top:74px;display:flex;gap:38px;font-size:12.5px;font-weight:600;color:#444;letter-spacing:.3px}
.main-nav .active{position:relative}
.main-nav .active::after{content:"";position:absolute;left:-6px;right:-6px;bottom:-14px;height:3px;background:var(--orange)}

/* hero */
.hero{top:130px;height:540px}
.hero-photo{position:absolute;inset:0;background:linear-gradient(180deg,#4a7fb6 0%,#9cb9d6 30%,#d8e2ea 45%,#7a8f6a 62%,#4d6a33 78%,#355222 100%)}
.play{position:absolute;left:573px;top:227px;width:54px;height:38px;border-radius:9px;background:#fff}
.play::after{content:"";position:absolute;left:22px;top:11px;border-left:14px solid #444;border-top:8px solid transparent;border-bottom:8px solid transparent}
.dots{position:absolute;left:566px;top:430px;display:flex;gap:8px}
.dots i{width:11px;height:11px;border-radius:50%;background:#fff;display:block}
.dots i.on{box-shadow:0 0 0 3px rgba(255,255,255,.5);background:#ddd}
.hero-wave{position:absolute;left:0;bottom:0;width:1200px;height:110px}

/* welcome */
.welcome{top:670px;height:541px}
.welcome h2{margin-top:66px}
.welcome .lead{width:840px;margin:26px auto 0;text-align:center;font-size:11.5px;line-height:21px;color:var(--muted)}
.services{position:absolute;top:236px;left:100px;width:1000px;display:flex;justify-content:space-between}
.service{width:310px;text-align:center}
.service-icon{width:116px;height:116px;border-radius:50%;background:var(--orange);margin:0 auto;position:relative;box-shadow:0 0 0 4px #fff inset,0 0 0 2px var(--orange)}
.service-icon::after{content:"";position:absolute;inset:38px;border:3px solid #fff;border-radius:8px}
.service h3{font-weight:400;font-size:19px;margin-top:22px;color:#333}
.service p{font-size:11.5px;line-height:21px;color:var(--muted);margin-top:14px;padding:0 10px}

/* products */
.products{top:1211px;height:636px}
.products-bg{position:absolute;inset:0;background:linear-gradient(135deg,var(--teal) 0%,#22808a 45%,var(--teal-dark) 100%)}
.products h2{color:#fff;padding-top:84px}
.product-row{position:absolute;left:98px;top:176px;display:flex;gap:22px}
.product-card{width:234px;height:342px;background:#fff;box-shadow:0 2px 6px rgba(0,0,0,.25)}
.product-photo{height:206px}
.p1{background:linear-gradient(160deg,#b45a3c,#e0826a,#8d3b2e)}
.p2{background:linear-gradient(160deg,#8f8c8a,#c9b9b2,#6a4a5e)}
.p3{background:linear-gradient(160deg,#d8cfc9,#a77f70,#5b4038)}
.p4{background:linear-gradient(160deg,#b48ad1,#e7b1c6,#f2e7d6)}
.product-card h4{font-weight:400;font-size:15.5px;text-align:center;margin-top:16px}
.product-card p{font-size:11px;line-height:18px;color:var(--muted);text-align:center;margin-top:8px;padding:0 28px}
.read-more{display:block;width:86px;margin:12px auto 0;border:1px solid #bbb;font-size:11px;text-align:center;padding:4px 0;color:#444}
.product-arrows{position:absolute;left:580px;top:576px}

/* news */
.news{top:1847px;height:589px;background:#fff}
.news-photo{position:absolute;right:0;top:0;width:610px;height:550px;background:linear-gradient(160deg,#ecd9cf 0%,#f2e6df 45%,#f6f3f1 100%)}
.news h2{position:absolute;left:98px;top:86px;font-family:"Roboto Condensed",sans-serif;font-weight:400;font-size:22px}
.news-arrows{position:absolute;left:536px;top:90px}
.news-item{position:absolute;left:98px;width:480px;display:flex;gap:26px}
.news-thumb{width:188px;height:148px;flex:none}
.n1{background:linear-gradient(140deg,#c44d79,#e7b7a4,#a2633f)}
.n2{background:linear-gradient(140deg,#8ab4d4,#c9d9e6,#6a8aa8)}
.news-item h5{font-weight:400;font-size:15px;color:#444}
.news-item .date{color:var(--blue);font-size:11.5px;font-weight:600;margin-top:20px}
.news-item p{font-size:11px;line-height:18px;color:var(--muted);margin-top:12px}
.news-item .more{font-size:11.5px;margin-top:12px;color:#333}

/* testimonials */
.testimonials{top:2436px;height:381px;background:var(--mist)}
.testimonials h2{margin-top:76px;font-size:30px}
.testimonials .rule{width:70px;height:3px;background:var(--blue);margin:14px auto 0}
.quote{position:absolute;top:180px;width:450px;display:flex;gap:22px}
.avatar{width:122px;height:122px;border-radius:50%;background:linear-gradient(160deg,#c6d2dc,#a98a74);border:3px solid #fff;box-shadow:0 0 0 1px #ccc;flex:none}
.quote p{font-style:italic;font-size:11px;line-height:19px;color:#555;margin-top:4px}
.quote .who{font-style:italic;font-size:12px;color:#1f5f99;margin-top:10px;line-height:17px}

/* subscribe */
.subscribe{top:2817px;height:165px;background:linear-gradient(90deg,var(--blue-dark),var(--blue) 60%,#1b7fc0)}
.subscribe h3{position:absolute;left:272px;top:62px;font-family:"Roboto Condensed",sans-serif;font-weight:700;font-size:19px;color:#fff;line-height:24px}
.sub-form{position:absolute;left:594px;top:64px;display:flex}
.sub-form .field{width:374px;height:42px;background:#fff;border-radius:21px 0 0 21px;font-size:12px;color:#777;padding:12px 22px}
.sub-form .btn{width:126px;height:42px;background:var(--dark);border-radius:0 21px 21px 0;color:#fff;font-size:12px;font-weight:600;text-align:center;line-height:42px}

/* footer */
.site-footer{top:2982px;height:308px;background:#fff}
.footer-col{position:absolute;top:55px}
.footer-col h6{font-family:"Roboto Condensed",sans-serif;font-weight:400;font-size:19px;color:#333}
.enquiry{left:98px;width:302px}
.enquiry .row{display:flex;gap:8px;margin-top:20px}
.enquiry .input{border:1px solid var(--line);height:36px;flex:1;font-size:10.5px;color:#555;padding:10px 8px}
.enquiry .msg{border:1px solid var(--line);height:70px;margin-top:10px;font-size:10.5px;color:#555;padding:8px}
.enquiry .submit{display:inline-block;margin-top:12px;background:var(--blue-dark);color:#fff;font-size:13px;font-weight:700;padding:7px 18px}
.contact{left:457px;width:300px}
.contact .line{display:flex;gap:14px;font-size:12px;color:#444;margin-top:20px;line-height:19px}
.contact svg{flex:none;margin-top:2px}
.quick-links{left:770px}
.quick-links ul{list-style:none;margin-top:16px}
.quick-links li{font-size:11px;color:#444;display:flex;align-items:center;gap:12px;height:21px}
.quick-links li::before{content:"";width:10px;height:10px;border-radius:50%;background:#444}
.footer-brand{position:absolute;left:920px;top:108px;display:flex;align-items:center;gap:10px}
.footer-brand .brand-mark{width:26px;height:26px}
.footer-brand .brand-name{font-size:28px}
.copyright{top:3290px;height:56px;border-top:1px solid #e5e5e5;text-align:center;font-size:11px;color:#555;padding-top:22px}
</style>
</head>
<body>

<header class="section site-header">
  <div class="utility-bar">
    <div class="utility-links">
      <span><svg width="10" height="12" viewBox="0 0 10 12"><rect x="1" y="5" width="8" height="7" fill="#fff"/><path d="M3 5V3a2 2 0 0 1 4 0v2" stroke="#fff" fill="none" stroke-width="1.4"/></svg>Sign In</span>
      <span><svg width="11" height="11" viewBox="0 0 11 11"><circle cx="5.5" cy="3" r="2.6" fill="#fff"/><path d="M0 11a5.5 5 0 0 1 11 0z" fill="#fff"/></svg>Registered</span>
      <span class="basket">View Basket</span>
    </div>
  </div>
  <div class="brand"><span class="brand-mark"></span><span class="brand-name">Mondeko</span></div>
  <nav class="main-nav">
    <span class="active">HOME</span><span>ABOUT US</span><span>SERVICES</span><span>PRODUCTS</span><span>BLOG</span><span>CONTACT US</span>
  </nav>
</header>

<section class="section hero">
  <div class="hero-photo" role="img" aria-label="Mountain valley with forested slopes under a bright sky full of clouds"></div>
  <div class="play"></div>
  <div class="dots"><i class="on"></i><i></i><i></i><i></i></div>
  <svg class="hero-wave" viewBox="0 0 1200 110" preserveAspectRatio="none">
    <path d="M0 70 C300 20 700 20 1200 55 L1200 110 L0 110Z" fill="#fff"/>
    <path d="M0 58 C300 8 700 10 1200 40" stroke="#1a86c8" stroke-width="9" fill="none"/>
    <path d="M0 74 C320 24 720 26 1200 58" stroke="#f7a21b" stroke-width="7" fill="none"/>
  </svg>
</section>

<section class="section welcome">
  <h2 class="section-title">WELCOME TO MONDEKO</h2>
  <p class="lead">Sed ut perspiciatis unde omnis iste natus error sit voluptatem accusantium doloremque laudantium, totam rem aperiam, eaque ipsa quae ab illo inventore veritatis et quasi architecto beatae vitae dicta sunt explicabo. Nemo enim ipsam voluptatem quia voluptas sit aspernatur aut odit aut fugit, sed quia consequuntur magni dolores eos qui ratione voluptatem sequi nesciunt. Neque porro quisquam est, qui dolorem ipsum quia dolor sit amet.</p>
  <div class="services">
    <div class="service"><div class="service-icon"></div><h3>Care Home</h3><p>Sed ut perspiciatis unde omnis iste natus error sit voluptatem accusantium doloremque laudantium, totam rem aperiam, eaque ipsa quae</p></div>
    <div class="service"><div class="service-icon"></div><h3>Nail Bar Industry</h3><p>Sed ut perspiciatis unde omnis iste natus error sit voluptatem accusantium doloremque laudantium, totam rem aperiam, eaque ipsa quae</p></div>
    <div class="service"><div class="service-icon"></div><h3>Skin Care Services</h3><p>Sed ut perspiciatis unde omnis iste natus error sit voluptatem accusantium doloremque laudantium, totam rem aperiam, eaque ipsa quae</p></div>
  </div>
</section>

<section class="section products">
  <div class="products-bg" role="img" aria-label="Teal pool water background"></div>
  <h2 class="section-title">OUR PRODUCTS</h2>
  <div class="product-row">
    <article class="product-card"><div class="product-photo p1" role="img" aria-label="Red nail polish bottles beside a UV nail lamp"></div><h4>Sed ut perspiciatis</h4><p>Nam libero tempore, cum soluta nobis est eligendi optio</p><span class="read-more">Read More</span></article>
    <article class="product-card"><div class="product-photo p2" role="img" aria-label="Manicure tools and polish bottles on a table"></div><h4>Sed ut perspiciatis</h4><p>Nam libero tempore, cum soluta nobis est eligendi optio</p><span class="read-more">Read More</span></article>
    <article class="product-card"><div class="product-photo p3" role="img" aria-label="Pedicure being applied to toenails"></div><h4>Sed ut perspiciatis</h4><p>Nam libero tempore, cum soluta nobis est eligendi optio</p><span class="read-more">Read More</span></article>
    <article class="product-card"><div class="product-photo p4" role="img" aria-label="Spa set with pumice, polish and towels"></div><h4>Sed ut perspiciatis</h4><p>Nam libero tempore, cum soluta nobis est eligendi optio</p><span class="read-more">Read More</span></article>
  </div>
  <svg class="product-arrows" width="40" height="24" viewBox="0 0 40 24"><path d="M14 4 6 12l8 8M26 4l8 8-8 8" stroke="#fff" stroke-width="3" fill="none"/></svg>
</section>

<section class="section news">
  <div class="news-photo" role="img" aria-label="Photograph: hands holding a flower above pedicured feet on a white towel"></div>
  <h2>LATEST NEWS</h2>
  <svg class="news-arrows" width="26" height="14" viewBox="0 0 26 14"><path d="M9 2 4 7l5 5M17 2l5 5-5 5" stroke="#333" stroke-width="2" fill="none"/></svg>
  <article class="news-item" style="top:156px">
    <div class="news-thumb n1" role="img" aria-label="Pedicured feet beside pink flowers"></div>
    <div><h5>Nulla at diam ornare, aliquam urna</h5><div class="date">APRIL 25, 2017</div><p>Nulla at diam ornare, aliquam urna vel, commodo urna. Nam id risus a est luctus consectetur quis eget libero. Suspendisse potenti.</p><div class="more">Read More +</div></div>
  </article>
  <article class="news-item" style="top:333px">
    <div class="news-thumb n2" role="img" aria-label="Nail polish being applied on a blue background"></div>
    <div><h5>Nulla at diam ornare, aliquam urna</h5><div class="date">APRIL 25, 2017</div><p>Nulla at diam ornare, aliquam urna vel, commodo urna. Nam id risus a est luctus consectetur quis eget libero. Suspendisse potenti.</p><div class="more">Read More +</div></div>
  </article>
</section>

<section class="section testimonials">
  <h2 class="section-title">TESTIMONIALS</h2>
  <div class="rule"></div>
  <div class="quote" style="left:98px">
    <div class="avatar" role="img" aria-label="Customer portrait"></div>
    <div><p>“ Sed ut perspiciatis unde omnis iste natus error sit voluptatem accusantium doloremque laudantium, totam rem aperiam, eaque ipsa quae ab illo inventore veritatis et quasi architecto beatae vitae dicta sunt explicabo. Nemo enim ipsam.</p><div class="who">Alan Pike-<br>Mondeko</div></div>
  </div>
  <div class="quote" style="left:636px">
    <div class="avatar" role="img" aria-label="Customer portrait"></div>
    <div><p>“ Sed ut perspiciatis unde omnis iste natus error sit voluptatem accusantium doloremque laudantium, totam rem aperiam, eaque ipsa quae ab illo inventore veritatis et quasi architecto beatae vitae dicta sunt explicabo. Nemo enim ipsam.</p><div class="who">Alan Pike-<br>Mondeko</div></div>
  </div>
</section>

<section class="section subscribe">
  <h3>SUBSCRIBE TO RECEIVE UPDATES AND<br>EXCLUSIVE OFFERS.</h3>
  <div class="sub-form"><div class="field">Enter your E - mail</div><div class="btn">SUBSCRIBE</div></div>
</section>

<footer class="section site-footer">
  <div class="footer-col enquiry">
    <h6>QUICK ENQUIRY</h6>
    <div class="row"><div class="input">Name</div><div class="input">Phone</div></div>
    <div class="msg">Message</div>
    <span class="submit">SUBMIT</span>
  </div>
  <div class="footer-col contact">
    <h6>CONTACT US</h6>
    <div class="line"><svg width="12" height="16" viewBox="0 0 12 16"><path d="M6 0a6 6 0 0 1 6 6c0 4-6 10-6 10S0 10 0 6a6 6 0 0 1 6-6z" fill="#1a86c8"/><circle cx="6" cy="6" r="2.2" fill="#fff"/></svg><span>Mondeko Ltd<br>4820 W Larkin Ave, Suite 12B,<br>Fenwick, OR 97411</span></div>
    <div class="line"><svg width="14" height="14" viewBox="0 0 14 14"><path d="M3 0l3 3-2 2a9 9 0 0 0 5 5l2-2 3 3-2 3C6 14 0 8 0 3z" fill="#1a86c8"/></svg><span>Phone: 555-017-2284</span></div>
    <div class="line"><svg width="15" height="11" viewBox="0 0 15 11"><rect width="15" height="11" fill="#1a86c8"/><path d="M0 0l7.5 6L15 0" stroke="#fff" fill="none"/></svg><span>Email: info@mondeko.com</span></div>
  </div>
  <div class="footer-col quick-links">
    <h6>QUICK LINKS</h6>
    <ul><li>Home</li><li>About Us</li><li>Services</li><li>Products</li><li>Blog</li><li>Contact</li></ul>
  </div>
  <div class="footer-brand"><span class="brand-mark"></span><span class="brand-name">Mondeko</span></div>
</footer>

<div class="section copyright">Copyright © 2017 Mondeko Ltd.All Right Reserved</div>

</body>
</html>
```